Exciting Personal Development Book Cover: FIND ZEN NOW!

Design a Book Cover for my personal development book.
Title: Find Zen Now!
Author: Marcus Telly
Tagline: A real-life solution to get unstuck and break free

My picture must make up the front cover as I need to build my brand and people should recognise me on book shelves. Bold and catchy. How you do it is up to you. There must be space for a short testimonial from a famous person who is currently reading my book. I uploaded a sample of what I made in Photoshop but I don't have design skills.

I've added a PDF of my book so you can read the chapter index and introduction to get a sense of the content.

Target Market(s)

Personal Development Self-Help Market

Industry/Entity Type

Personal Development

Font styles to use
Serif
Sans Serif

Requirements
Must have
• My picture as hero image on cover.
Nice to have
• Must have Title, Tagline and my author name. If possible ZEN stands for 'Zeal, Energy & Nerve' If there is a way to fit this somewhere great. If it's too much then it can go somewhere on the back.

```html
<!DOCTYPE html>
<html lang="en">
<head>
<meta charset="utf-8">
<title>Find Zen Now! — Marcus Telly</title>
<link rel="stylesheet" href="https://fonts.googleapis.com/css2?family=Anton&family=Oswald:wght@400;500&display=swap">
<style>
  :root {
    --page: #e6e7e7;
    --cover-deep: #032a31;
    --cover-mid: #0b3a43;
    --cover-glow: #1e4a3b;
    --title-top: #ffffff;
    --title-bottom: #959ea4;
    --gold: #ecc57c;
    --maroon: #4a0f16;
    --tag: #dc8d6b;
    --tag-fold: #8a4a33;
    --tag-text: #2b140e;
    --skin: #c49479;
    --shirt: #efede9;
  }
  * { margin: 0; padding: 0; box-sizing: border-box; }
  html, body {
    width: 1084px; height: 1200px; overflow: hidden;
    background: var(--page);
  }
  .book-cover {
    position: absolute; left: 212px; top: 25px;
    width: 660px; height: 1150px; overflow: hidden;
    background:
      radial-gradient(ellipse 260px 320px at 470px 560px, var(--cover-glow), transparent 75%),
      linear-gradient(135deg, var(--cover-mid) 0%, var(--cover-deep) 70%);
    box-shadow: 0 18px 40px rgba(0,0,0,.25);
  }
  .author-portrait {
    position: absolute; left: 101px; top: 336px;
    width: 446px; height: 814px;
    border-radius: 180px 180px 0 0;
    background:
      radial-gradient(ellipse 90px 120px at 250px 150px, var(--skin) 0%, transparent 100%),
      linear-gradient(180deg, rgba(196,148,121,0) 0%, var(--shirt) 45%, var(--shirt) 100%);
    opacity: .92;
  }
  .cover-art { position: absolute; inset: 0; }
  .title-line {
    font-family: "Anton", "Oswald", sans-serif;
  }
  .acronym-tag text {
    font-family: "Oswald", sans-serif; font-weight: 500;
    font-size: 19px; fill: var(--tag-text);
  }
  .tagline {
    position: absolute; left: 436px; top: 398px;
    font-family: "Oswald", sans-serif; font-weight: 400;
    font-size: 28px; line-height: 38px; color: var(--gold);
    white-space: nowrap;
  }
  .author-name {
    font-family: "Anton", "Oswald", sans-serif;
    fill: var(--gold); stroke: var(--maroon); stroke-width: 3px;
    paint-order: stroke fill;
  }
</style>
</head>
<body>
  <main class="book-cover">
    <div class="author-portrait" role="img" aria-label="Photograph of the author smiling, wearing a white shirt with sleeves rolled up and tattooed forearms"></div>

    <svg class="cover-art" width="660" height="1150" viewBox="0 0 660 1150">
      <defs>
        <linearGradient id="titleFill" x1="0" y1="0" x2="0" y2="1">
          <stop offset="0" stop-color="#ffffff"/>
          <stop offset=".55" stop-color="#ffffff"/>
          <stop offset="1" stop-color="#959ea4"/>
        </linearGradient>
      </defs>

      <text class="title-line" x="64" y="332" font-size="290" textLength="534" lengthAdjust="spacingAndGlyphs" fill="url(#titleFill)">FIND ZEN</text>
      <text class="title-line" x="66" y="592" font-size="273" textLength="228" lengthAdjust="spacingAndGlyphs" fill="url(#titleFill)">NOW!</text>

      <g class="acronym-tag" transform="translate(424 158)">
        <polygon points="0,3 6,0 86,0 94,12 86,25 0,25" fill="var(--tag)"/>
        <polygon points="0,3 6,0 6,25 0,28" fill="var(--tag-fold)"/>
        <text x="47" y="19" text-anchor="middle">Energy</text>
      </g>
      <g class="acronym-tag" transform="translate(320 264)">
        <polygon points="0,3 6,0 86,0 94,12 86,25 0,25" fill="var(--tag)"/>
        <polygon points="0,3 6,0 6,25 0,28" fill="var(--tag-fold)"/>
        <text x="47" y="19" text-anchor="middle">Zeal</text>
      </g>
      <g class="acronym-tag" transform="translate(506 288)">
        <polygon points="0,3 6,0 86,0 94,12 86,25 0,25" fill="var(--tag)"/>
        <polygon points="0,3 6,0 6,25 0,28" fill="var(--tag-fold)"/>
        <text x="47" y="19" text-anchor="middle">Nerve</text>
      </g>

      <text class="author-name" x="417" y="980" font-size="88" textLength="182" lengthAdjust="spacingAndGlyphs">MARCUS</text>
      <text class="author-name" x="417" y="1066" font-size="88" textLength="160" lengthAdjust="spacingAndGlyphs">TELLY</text>
    </svg>

    <p class="tagline">A real-life<br>solution to get<br>unstuck and<br>break free</p>
  </main>
</body>
</html>
```